Good Morning Banner

We need a banner design (20.4 x 10.14) with the words 'Good Morning' as the main feature and the words 'Prophet K.O. Adelani' underneath. Attached is an example but let your creative juices flow!

Target Market(s)

Christian

```html
<!DOCTYPE html>
<html lang="en">
<head>
<meta charset="utf-8">
<title>Good Morning Banner</title>
<link rel="stylesheet" href="https://fonts.googleapis.com/css2?family=Archivo+Black&family=Roboto:wght@300;500&family=Roboto+Condensed:wght@300&display=swap">
<style>
  :root {
    --ocean-deep: #22397f;
    --ocean-mid: #3b5aa8;
    --white: #ffffff;
    --gold: #ffc800;
    --band: rgba(34, 42, 66, 0.85);
  }
  html, body {
    margin: 0;
    padding: 0;
    overflow: hidden;
    background: var(--ocean-deep);
  }
  .banner {
    position: relative;
    width: 1200px;
    height: 597px;
    overflow: hidden;
    font-family: "Roboto", Arial, sans-serif;
  }
  .world-map {
    position: absolute;
    inset: 0;
    background:
      radial-gradient(ellipse 30% 35% at 25% 30%, rgba(123,111,154,0.55), transparent 70%),
      radial-gradient(ellipse 35% 30% at 70% 25%, rgba(123,111,154,0.55), transparent 70%),
      radial-gradient(ellipse 14% 25% at 35% 72%, rgba(123,111,154,0.45), transparent 70%),
      radial-gradient(ellipse 15% 22% at 55% 60%, rgba(123,111,154,0.45), transparent 70%),
      radial-gradient(ellipse 9% 10% at 87% 75%, rgba(123,111,154,0.45), transparent 70%),
      linear-gradient(180deg, var(--ocean-mid) 0%, var(--ocean-deep) 100%);
  }
  .headline {
    position: absolute;
    left: 0;
    width: 1200px;
    top: 203px;
    margin: 0;
    text-align: center;
    font-family: "Archivo Black", "Arial Black", sans-serif;
    font-weight: 400;
    font-size: 122px;
    line-height: 1;
    letter-spacing: -1.5px;
    text-shadow: 4px 6px 10px rgba(0,0,0,0.45);
  }
  .headline .good { color: var(--white); }
  .headline .morning { color: var(--gold); }
  .speaker {
    position: absolute;
    right: 107px;
    top: 326px;
    margin: 0;
    color: var(--white);
    font-family: "Roboto Condensed", "Arial Narrow", sans-serif;
    font-weight: 300;
    font-size: 36px;
    line-height: 1.1;
    letter-spacing: 3px;
    text-transform: uppercase;
  }
  .footer-band {
    position: absolute;
    left: 0;
    bottom: 0;
    width: 1200px;
    height: 67px;
    background: var(--band);
  }
  .ministry-name {
    position: absolute;
    left: 77px;
    top: 22px;
    color: var(--white);
    font-weight: 300;
    font-size: 22px;
    line-height: 1;
    letter-spacing: 3px;
    text-transform: uppercase;
  }
  .contact {
    position: absolute;
    top: 21px;
    display: flex;
    align-items: center;
    gap: 10px;
    color: var(--gold);
    font-weight: 500;
    font-size: 23px;
    line-height: 1;
  }
  .contact-web { left: 640px; }
  .contact-social { left: 922px; }
  .contact svg { width: 22px; height: 22px; }
</style>
</head>
<body>
  <div class="banner">
    <div class="world-map" role="img" aria-label="Relief map of the world in blue and muted purple tones"></div>

    <h1 class="headline"><span class="good">GOOD</span><span class="morning">MORNING</span></h1>
    <p class="speaker">Prophet K.O. Adelani</p>

    <div class="footer-band">
      <span class="ministry-name">Dawnlight Fellowship</span>

      <div class="contact contact-web">
        <svg viewBox="0 0 24 24" aria-hidden="true">
          <g fill="none" stroke="#ffc800" stroke-width="1.6">
            <circle cx="12" cy="12" r="10"/>
            <ellipse cx="12" cy="12" rx="4.5" ry="10"/>
            <line x1="2" y1="12" x2="22" y2="12"/>
            <path d="M4 7h16M4 17h16"/>
          </g>
        </svg>
        <span>www.dawnlight.org</span>
      </div>

      <div class="contact contact-social">
        <svg viewBox="0 0 24 24" aria-hidden="true">
          <circle cx="12" cy="12" r="10" fill="none" stroke="#ffc800" stroke-width="1.6"/>
        </svg>
        <span>dawnlightchurch</span>
      </div>
    </div>
  </div>
</body>
</html>
```